Used Car Business Card Design

Maple Ridge Auto Sales is a woman owned women friendly car lot.  We focus on providing Professionalism, Integrity and Respect beginning with the initial introduction.  We place the highest importance on customer service after the sale and our rating with the Fair Trade Bureau of Arkansas shows it.  We're starting out 7th year, recently relocated. Satisfied Clients bring their family members, friends and co-workers to buy their cars, SUV's and trucks from MRAS.
You buy here / you pay here, Lending program opportunities too, Great Cash Prices
Finance with Flexibility we look at each individual uniquely and not a credit score
I think of my kids when getting our vehicles ready and your safety when you drive away in a MRAS car. . .  Drive away with Peace of Mind...
Maroon, Black and Silver colors.

Updates
I sent a response to the designers - have  not heard from them, will I receive my funds back?

Thank you all,  a lot of great designs - Making my decision on Nov 4th

So much talent. . .
So very challenging. . .
Thank you for your participation.
Sincerely,
Maple Ridge Auto Sales
Lorna Pettigrew

Industry/Entity Type
Safety
Contact Information for Business Card
Maple Ridge Auto Sales
"A Steady Car for a Steady Price"
4153 Oakvale Rd. Pine Hollow, Ar 72055
Lorna Pettigrew
501.739.2018

```html
<!DOCTYPE html>
<html lang="en">
<head>
<meta charset="utf-8">
<title>Maple Ridge Auto Sales – Business Cards</title>
<link rel="stylesheet" href="https://fonts.googleapis.com/css2?family=Fira+Sans:ital,wght@0,300;0,400;0,800;1,300&display=swap">
<style>
  :root{
    --backdrop:#e6e8e6;
    --card:#ffffff;
    --maroon:#26101a;
    --ink:#1d1d1d;
    --rule:#1a1a1a;
    --on-maroon:#f4eef0;
  }
  *{box-sizing:border-box;margin:0;padding:0}
  html,body{width:1200px;height:1000px;overflow:hidden;background:var(--backdrop)}
  body{font-family:"Fira Sans",sans-serif;position:relative}

  .card{
    position:absolute;left:250px;width:700px;height:400px;
    background:var(--card);overflow:hidden;
    box-shadow:0 4px 18px rgba(0,0,0,.18);
  }
  .card--front{top:70px}
  .card--back{top:530px}

  .brand-name{
    font-family:"Fira Sans",sans-serif;font-weight:800;
    color:var(--maroon);font-size:44px;letter-spacing:-0.5px;
    white-space:nowrap;position:absolute;line-height:1.2;
  }
  .tagline{
    position:absolute;font-family:"Fira Sans",sans-serif;
    font-style:italic;font-weight:300;color:var(--ink);
    white-space:nowrap;letter-spacing:.5px;line-height:1.2;
  }

  /* front */
  .front-band{
    position:absolute;left:0;top:0;width:100%;height:272px;background:var(--maroon);
  }
  .card--front .brand-name{left:44px;top:26px;color:var(--on-maroon)}
  .contact{
    position:absolute;right:60px;top:104px;text-align:right;
    color:var(--on-maroon);font-weight:300;line-height:1.22;
  }
  .contact__name{font-size:30px;font-weight:400}
  .contact__phone{font-size:26px;margin-bottom:8px}
  .contact__address{font-size:24px}
  .card--front .tagline{right:60px;top:300px;font-size:26px}

  /* back */
  .rule{position:absolute;left:0;width:100%;height:3px;background:var(--rule)}
  .rule--top{top:34px}
  .rule--bottom{top:142px}
  .card--back .brand-name{left:50px;top:58px}
  .card--back .tagline{left:50px;top:200px;font-size:30px}
</style>
</head>
<body>
  <section class="card card--front" aria-label="Business card front">
    <div class="front-band"></div>
    <div class="brand-name">Maple Ridge Auto Sales</div>
    <div class="contact">
      <div class="contact__name">Lorna Pettigrew</div>
      <div class="contact__phone">501.739.2018</div>
      <div class="contact__address">4153 Oakvale Rd.</div>
      <div class="contact__address">Pine Hollow, Ar 72055</div>
    </div>
    <div class="tagline">- A Steady Car for a Steady Price -</div>
  </section>

  <section class="card card--back" aria-label="Business card back">
    <div class="rule rule--top"></div>
    <div class="brand-name">Maple Ridge Auto Sales</div>
    <div class="rule rule--bottom"></div>
    <div class="tagline">- A Steady Car for a Steady Price -</div>
  </section>
</body>
</html>
```